Webpage layout and company logo combination

We are trying to renovate an existing site to make it sharper and sophisticated in appearance. This is the existing site: http://www.kestrelhomesnj.com/agents.html . The new presentation should be bright, sharp, sophisticated and should incorporate two additional menu tabs. The menu tabs will be revised as follows: Property Listings, Property Management, Advisory & Consulting, Local Info, R/E Tools, Our Team (please disregard Korean language characters, which will be installed after English version is completed, separately).

It Company

```html
<!DOCTYPE html>
<html lang="en">
<head>
<meta charset="utf-8">
<title>Kestrel Homes</title>
<link href="https://fonts.googleapis.com/css2?family=Arimo:wght@400;700&display=swap" rel="stylesheet">
<style>
:root{
  --green:#79c51e;
  --green-dark:#4e9a0c;
  --purple:#574c9e;
  --purple-dark:#4b418d;
  --footer:#4d4a72;
  --footer-dark:#3d3a60;
  --panel:#ececec;
  --line:#d4d4d4;
  --text:#333;
  --muted:#8a8a8a;
  --white:#fff;
}
*{box-sizing:border-box;margin:0;padding:0}
html,body{width:857px;height:1200px;overflow:hidden;background:#fff}
body{position:relative;font-family:"Arimo",Arial,sans-serif;color:var(--text)}
.abs{position:absolute}

.topbar{left:0;top:0;width:857px;height:30px;background:#f4f4f4;border-bottom:1px solid #e2e2e2}
.topbar .phone{left:63px;top:8px;font-size:12px;color:#999;display:flex;align-items:center;gap:6px}
.social{display:flex;gap:10px}
.social span{width:12px;height:12px;border-radius:50%;background:#aaa;display:block}
.topbar .social{right:64px;top:9px}

.header{left:0;top:30px;width:857px;height:50px;background:#fff}
.brand{display:flex;align-items:center;gap:6px;font-size:14px;font-weight:700;color:var(--green);letter-spacing:.2px}
.brand i{width:18px;height:18px;background:var(--green);display:block}
.header .brand{left:63px;top:15px}
.nav{left:235px;top:18px;display:flex;gap:12px;font-size:10.2px;color:#333;text-transform:uppercase;letter-spacing:.1px}
.nav-active{left:243px;top:47px;width:83px;height:4px;background:var(--green)}

.hero{left:0;top:80px;width:857px;height:360px;background:linear-gradient(180deg,#3a3430 0%,#6b5a4c 35%,#3b2a22 70%,#2a1d18 100%)}
.hero h1{position:absolute;left:93px;top:78px;font-size:40px;font-weight:400;line-height:42px;color:#fff;letter-spacing:-.5px}
.hero h1 em{font-style:normal;color:var(--green);display:block}
.arrow{width:46px;height:46px;border:2px solid rgba(255,255,255,.8);border-radius:50%;top:157px}

.tabs{left:43px;top:388px;width:771px;height:52px;background:var(--purple);display:flex;font-size:11px;color:#fff;text-transform:uppercase}
.tabs div{display:flex;align-items:center;justify-content:center;width:147px;border-right:1px solid #4a4088}
.tabs .on{background:var(--purple-dark)}
.tabs .spacer{flex:1}
.tabs .all{background:var(--purple-dark);border:none;width:147px}

.search{left:43px;top:440px;width:771px;height:171px;background:var(--panel);border:1px solid var(--line);border-top:none}
.lbl{font-size:11px;color:#333}
.select{height:30px;background:#e0e0e0;border:1px solid #cfcfcf;font-size:12px;color:#888;padding:8px 0 0 14px}
.select::after{content:"";position:absolute;right:0;top:0;width:32px;height:28px;border-left:1px solid #cfcfcf;background:linear-gradient(#aaa,#aaa) no-repeat}
.caret{position:absolute;right:11px;top:12px;width:0;height:0;border:5px solid transparent;border-top:6px solid #9a9a9a}
.pill{background:#d8d8d8;border-radius:3px;font-size:9px;padding:3px 8px;color:#333}
.btn{background:linear-gradient(#7dcb1f,#4f9b0d);color:#fff;font-size:9.5px;font-weight:700;text-align:center;border-radius:2px}

.section-title{left:43px;top:628px;font-size:14px;color:#444}
.rule{left:43px;top:650px;width:771px;height:1px;background:#bbb}
.rule-accent{left:43px;top:648px;width:140px;height:5px;background:var(--purple)}

.band{left:0;top:672px;width:857px;height:256px;background:var(--panel);border-top:1px solid var(--line);border-bottom:1px solid var(--line)}
.card{top:684px;width:172px;height:226px;background:#fff;border:1px solid #ddd}
.card .photo{position:absolute;left:8px;top:8px;width:155px;height:102px}
.card .tag{position:absolute;left:8px;top:8px;background:var(--purple);color:#fff;font-size:6.5px;padding:6px 5px;text-transform:uppercase}
.card .street{position:absolute;left:8px;top:120px;font-size:9.5px;font-weight:700;color:#444}
.card .city{position:absolute;left:8px;top:135px;font-size:9px;color:#888}
.card .sep{position:absolute;left:8px;top:154px;width:155px;height:1px;background:#bbb}
.card .status{position:absolute;left:8px;top:167px;background:#ddd;color:#fff;font-size:7px;padding:4px 8px;text-transform:uppercase}
.card .price{position:absolute;right:9px;top:167px;font-size:14px;font-weight:700;color:var(--purple)}
.card .meta{position:absolute;left:0;bottom:0;width:170px;height:26px;border-top:1px solid #e2e2e2;display:flex;font-size:7px;color:#999}
.card .meta span{flex:1;display:flex;align-items:center;justify-content:center;border-right:1px solid #e2e2e2}
.card .meta span:last-child{border:none}

.footer{left:0;top:973px;width:857px;height:197px;background:var(--footer);color:#fff}
.footer h3{position:absolute;font-size:13px;font-weight:400}
.footer p{position:absolute;font-size:10px;line-height:15.5px;color:#dcdbe8}
.contact{position:absolute;left:336px;font-size:10px;color:#dcdbe8;display:flex;gap:8px;line-height:17px}
.email{left:584px;top:121px;width:122px;height:28px;background:#fff;font-size:12px;color:#999;padding:7px 10px}
.bottombar{left:0;top:1170px;width:857px;height:30px;background:var(--footer-dark)}
.bottombar .copy{left:70px;top:12px;font-size:7.5px;color:#b9b7cf}
.bottombar .social{right:74px;top:10px}
.bottombar .social span{background:#c8c6dc}
</style>
</head>
<body>

<div class="abs topbar">
  <div class="abs phone">
    <svg width="11" height="11" viewBox="0 0 24 24"><path fill="#aaa" d="M6.6 10.8a15 15 0 0 0 6.6 6.6l2.2-2.2c.3-.3.7-.4 1-.2 1.1.4 2.3.6 3.6.6.6 0 1 .4 1 1V20c0 .6-.4 1-1 1A17 17 0 0 1 3 4c0-.6.4-1 1-1h3.5c.6 0 1 .4 1 1 0 1.3.2 2.5.6 3.6.1.3 0 .7-.2 1z"/></svg>
    (866)555-0142
  </div>
  <div class="abs social"><span></span><span></span><span></span><span></span></div>
</div>

<div class="abs header">
  <div class="abs brand"><i></i>KESTREL HOMES</div>
  <nav class="abs nav">
    <span>Property Listings</span><span>Property Management</span><span>Advisory &amp; Consulting</span><span>Local Info</span><span>R/E Tools</span><span>Our Team</span>
  </nav>
  <div class="abs nav-active"></div>
</div>

<section class="abs hero" role="img" aria-label="Modern loft living room with white sofa, fireplace and city view at dusk">
  <h1>Find The House of<em>Your Dreams</em></h1>
  <svg class="abs arrow" style="left:18px" viewBox="0 0 46 46"><path d="M26 14l-9 9 9 9" fill="none" stroke="#fff" stroke-width="2"/></svg>
  <svg class="abs arrow" style="left:792px" viewBox="0 0 46 46"><path d="M20 14l9 9-9 9" fill="none" stroke="#fff" stroke-width="2"/></svg>
</section>

<div class="abs tabs">
  <div class="on">All Properties</div><div>For Sale</div><div>For Rent</div><div class="spacer"></div><div class="all">View All Listings</div>
</div>

<form class="abs search">
  <span class="abs lbl" style="left:29px;top:23px">Property Type</span>
  <div class="abs select" style="left:29px;top:39px;width:218px">Any<span class="caret"></span></div>
  <span class="abs lbl" style="left:280px;top:23px">Location</span>
  <div class="abs select" style="left:280px;top:39px;width:218px">Any<span class="caret"></span></div>
  <span class="abs lbl" style="left:529px;top:23px">Price Range</span>
  <span class="abs pill" style="left:621px;top:20px">$150,000</span>
  <span class="abs lbl" style="left:681px;top:21px">-</span>
  <span class="abs pill" style="left:678px;top:20px;left:678px">$550,000</span>
  <svg class="abs" style="left:529px;top:42px" width="218" height="28" viewBox="0 0 218 28">
    <rect x="0" y="7" width="217" height="7" rx="3.5" fill="#e0e0e0" stroke="#c8c8c8"/>
    <rect x="40" y="7" width="92" height="7" fill="#79c51e"/>
    <circle cx="40" cy="10.5" r="9" fill="#f2f2f2" stroke="#999"/>
    <circle cx="132" cy="10.5" r="9" fill="#f2f2f2" stroke="#999"/>
    <text x="0" y="26" font-size="7" fill="#555" font-family="Arimo,sans-serif">0</text>
    <text x="217" y="26" font-size="7" fill="#555" text-anchor="end" font-family="Arimo,sans-serif">1.000.000</text>
  </svg>
  <span class="abs lbl" style="left:29px;top:93px">Beds</span>
  <div class="abs select" style="left:29px;top:109px;width:151px">Any<span class="caret"></span></div>
  <span class="abs lbl" style="left:213px;top:93px">Baths</span>
  <div class="abs select" style="left:213px;top:109px;width:151px">Any<span class="caret"></span></div>
  <span class="abs lbl" style="left:397px;top:93px">Area (Sq Ft)</span>
  <div class="abs select" style="left:397px;top:109px;width:151px">Any<span class="caret"></span></div>
  <div class="abs btn" style="left:588px;top:109px;width:158px;height:31px;line-height:31px">FIND PROPERTIES</div>
</form>

<h2 class="abs section-title" style="font-weight:400">RECENT PROPERTIES</h2>
<div class="abs rule"></div>
<div class="abs rule-accent"></div>

<div class="abs band"></div>

<article class="abs card" style="left:43px">
  <div class="photo" role="img" aria-label="Modern two-storey family home with timber and stone facade" style="background:linear-gradient(#d9e4ee,#7d6a58 60%,#9a9a92)"></div>
  <span class="tag">Family Home</span>
  <div class="street">214 Alder Avenue</div><div class="city">Millbrook, MD</div><div class="sep"></div>
  <span class="status">For Sale</span><span class="price">$687,000</span>
  <div class="meta"><span>2,412m</span><span>6 Beds</span><span>3 Baths</span></div>
</article>
<article class="abs card" style="left:243px">
  <div class="photo" role="img" aria-label="Shingled apartment house surrounded by greenery" style="background:linear-gradient(#cfe0ea,#8b7a5e 55%,#5f7a3e)"></div>
  <span class="tag">Apartment</span>
  <div class="street">214 Alder Avenue</div><div class="city">Millbrook, MD</div><div class="sep"></div>
  <span class="status">For Sale</span><span class="price">$1,200/mo</span>
  <div class="meta"><span>2,412m</span><span>6 Beds</span><span>3 Baths</span></div>
</article>
<article class="abs card" style="left:443px">
  <div class="photo" role="img" aria-label="Contemporary brick family house under blue sky" style="background:linear-gradient(#4f86c9,#8a6a54 55%,#6c6a60)"></div>
  <span class="tag">Family Home</span>
  <div class="street">214 Alder Avenue</div><div class="city">Millbrook, MD</div><div class="sep"></div>
  <span class="status">For Sale</span><span class="price">$587,000</span>
  <div class="meta"><span>2,412m</span><span>6 Beds</span><span>3 Baths</span></div>
</article>
<article class="abs card" style="left:643px">
  <div class="photo" role="img" aria-label="Victorian apartment houses along a tree-lined street" style="background:linear-gradient(#3f74c4,#b89a78 50%,#4f6a3a)"></div>
  <span class="tag">Apartment</span>
  <div class="street">214 Alder Avenue</div><div class="city">Millbrook, MD</div><div class="sep"></div>
  <span class="status">For Sale</span><span class="price">$887,000</span>
  <div class="meta"><span>2,412m</span><span>6 Beds</span><span>3 Baths</span></div>
</article>

<footer class="abs footer">
  <div class="abs brand" style="left:71px;top:36px"><i></i>KESTREL HOMES</div>
  <p style="left:71px;top:64px;width:210px">Lorem ipsum dolor amet, consectetur adipi-scing elit. Sed ut purus eget nunc ut dignis-sim cursus at a nisl. Mauris vitae turpis quis eros egestas tempor sit amet a arcu. Duis egestas hendrerit diam.</p>

  <h3 style="left:336px;top:36px">CONTACT</h3>
  <div class="contact" style="top:64px">
    <svg width="13" height="13" viewBox="0 0 24 24"><path fill="#b9b7cf" d="M6.6 10.8a15 15 0 0 0 6.6 6.6l2.2-2.2c.3-.3.7-.4 1-.2 1.1.4 2.3.6 3.6.6.6 0 1 .4 1 1V20c0 .6-.4 1-1 1A17 17 0 0 1 3 4c0-.6.4-1 1-1h3.5c.6 0 1 .4 1 1 0 1.3.2 2.5.6 3.6.1.3 0 .7-.2 1z"/></svg>
    <span>(866)555-0142<br>(201)555-0187</span>
  </div>
  <div class="contact" style="top:108px">
    <svg width="13" height="13" viewBox="0 0 24 24"><path fill="none" stroke="#b9b7cf" stroke-width="2" d="M12 22s7-7 7-12a7 7 0 0 0-14 0c0 5 7 12 7 12z"/><circle cx="12" cy="10" r="2.5" fill="#b9b7cf"/></svg>
    <span>418 Larkspur Terrace Glenbrook, NJ 07099</span>
  </div>
  <div class="contact" style="top:138px">
    <svg width="13" height="13" viewBox="0 0 24 24"><rect x="2" y="5" width="20" height="14" fill="none" stroke="#b9b7cf" stroke-width="2"/><path d="M2 6l10 7 10-7" fill="none" stroke="#b9b7cf" stroke-width="2"/></svg>
    <span>hello@kestrelhomes.example</span>
  </div>

  <h3 style="left:585px;top:36px">NEWSLETTER</h3>
  <p style="left:584px;top:64px;width:205px">Lorem ipsum dolor amet, consectetur adipi-scing elit. Sed ut purus eget nunc ut dignis-sim cursus at a nisl.</p>
  <div class="abs email">Your Email</div>
  <div class="abs btn" style="left:713px;top:121px;width:70px;height:28px;line-height:28px">SEND</div>
</footer>

<div class="abs bottombar">
  <span class="abs copy">© Copyright 2014 Kestrel Homes. All Rights Reserved</span>
  <div class="abs social"><span></span><span></span><span></span><span></span></div>
</div>

</body>
</html>
```